Flyer - Clearway Dental Marrowby

** Please do not use my words - word-for-word on the flyer design **
We have recently bought an established dental business. However we are not getting new customers through the door. We plan to implement aggressive local marketing strategies including flyer distribution. We are looking for an eye-catching must read flyer design. Some details & content ideas are as below.
1. A5 size - Double Sided
2. Our business name is Clearway Dental Marrowby. Logo is attached. Website is www.clearwaydentalmarrowby.example.au where lot of useful information can be found.
3. Practice has a long & proud history serving "Lower North Shore" since 1958. We provide quality dental care at affordable prices.
4. List of services can be found on website
5. Perhaps a snippet of Orbix Map Location would be useful. Also the fact that 3-hour free parking is available in Ferncroft Arcade less than 100m away from practice. Plenty of 2-hours street parking is available too.
6. Opening hours can be found on website. Fact that we are open on Saturdays and till late on Tuesdays is worth calling out.
7. We would like to run a campaign of offers with this flyer. Give it a name! Details below.
a) NO GAP Checkup and Clean with any major Private Health Fund. Includes oral exam, 2 X-Rays, Scale & Polish and Fluoride Treatment
b) Genuine Teeth Whitening for $199 (usually $399 save $200)
c) 10% off on all major dental. Includes fillings, crowns, bridges and root canal treatment
8. We are KEVO Preferred Provider means KEVO members get maximum benefit. KEVO Patient Circle logo attached.
9. We participate in Office of Civic Pensions Fee Schedule. Logo attached.
10. Call out WE ACCEPT ALL HEALTH FUNDS
Dental
- Helvetica Neue, Myriad Pro

```html
<!DOCTYPE html>
<html lang="en">
<head>
<meta charset="utf-8">
<title>Clearway Dental Marrowby – Flyer</title>
<link href="https://fonts.googleapis.com/css2?family=Arimo:ital,wght@0,400;0,700;1,700&family=Roboto+Condensed:ital,wght@0,400;0,700;1,700&display=swap" rel="stylesheet">
<style>
:root{
  --blue:#2a3d91;
  --lime:#c3d52c;
  --teal:#5dbfae;
  --red:#d8222b;
  --yellow:#eef05a;
  --ink:#1f1f1f;
  --text:#333;
  --bg:#e9e6e1;
  --paper:#ffffff;
}
*{margin:0;padding:0;box-sizing:border-box}
html,body{width:1200px;height:1078px;overflow:hidden}
body{background:var(--bg);font-family:"Arimo",Arial,sans-serif;color:var(--text);position:relative}
.flyer{position:absolute;width:530px;height:760px;background:var(--paper);overflow:hidden;box-shadow:0 6px 18px rgba(0,0,0,.25)}
.flyer-front{left:60px;top:60px}
.flyer-back{left:610px;top:258px;font-family:"Roboto Condensed","Arial Narrow",sans-serif}
.photo{position:absolute}

/* logo */
.brand{position:absolute;display:flex;align-items:center;gap:8px}
.brand-dot{width:30px;height:30px;border-radius:50%;background:var(--lime);flex:none}
.brand-name{color:#fff;font-family:"Arimo",Arial,sans-serif;font-weight:400;font-size:19px;line-height:1.05}

/* front */
.front-header{position:absolute;left:0;top:0;width:530px;height:125px}
.headline{position:absolute;left:26px;top:100px;color:var(--ink);font-weight:400}
.headline span{display:block;height:30px;line-height:30px}
.headline .sm{font-size:24px}
.headline .lg{font-size:34px}
.hero-photo{left:215px;top:125px;width:315px;height:235px;background:linear-gradient(135deg,#f1ddd0,#d9b49c 55%,#f4f1ee)}
.lips{left:40px;top:300px;width:96px;height:42px;border-radius:50%/40% 40% 60% 60%;background:var(--red)}
.intro{position:absolute;left:40px;top:380px;width:460px;font-size:12px;line-height:1.38}
.intro p{margin-bottom:10px}
.contact-title{position:absolute;left:40px;top:535px;font-size:26px;font-weight:400;color:var(--teal)}
.contact-title b{font-weight:700}
.contact-list{position:absolute;left:40px;top:576px;width:300px;font-size:11px;list-style:none}
.contact-list li{display:flex;gap:8px;align-items:flex-start;margin-bottom:6px;line-height:15px}
.contact-list svg{flex:none;width:14px;height:14px}
.contact-list .phone strong{font-size:13px}
.hours{display:grid;grid-template-columns:70px 1fr;font-size:10.5px;line-height:14px}
.smile-photo{left:345px;top:545px;width:170px;height:150px;background:linear-gradient(160deg,#f3e9e4,#d79a8c 50%,#fbf7f5)}
.front-band{position:absolute;left:0;bottom:0;width:530px;height:38px;background:var(--teal);display:flex;align-items:center;justify-content:center}
.front-band p{color:var(--blue);font-weight:700;font-style:italic;font-size:16.5px}

/* back */
.p1{left:22px;top:20px;width:108px;height:92px;background:linear-gradient(150deg,#9fc3d8,#e8edf1)}
.p2{left:8px;top:120px;width:140px;height:118px;background:linear-gradient(150deg,#c5d8e4,#6f8da2)}
.p3{left:8px;top:246px;width:140px;height:122px;background:linear-gradient(150deg,#a7cfe0,#f0e6df)}
.p4{left:22px;top:376px;width:112px;height:92px;background:linear-gradient(150deg,#dfe6ec,#8ea4b8)}
.doctor{left:156px;top:16px;width:135px;height:270px;background:linear-gradient(180deg,#ecf0f3,#c9d3dc)}
.services{position:absolute;left:305px;top:22px}
.services h2{font-size:21px;font-weight:700;color:var(--ink);margin-bottom:8px}
.services ul{list-style:none}
.services li{display:flex;align-items:center;gap:9px;font-size:15px;color:var(--ink);height:23.5px}
.services svg{width:16px;height:16px;flex:none}
.offers{position:absolute;left:152px;top:300px;width:362px;height:182px;border:4px dashed var(--lime);border-left:none}
.offers h2{position:absolute;left:70px;top:10px;font-size:20px;font-weight:700;color:var(--ink)}
.offer{position:absolute;left:8px;display:flex;gap:8px;color:var(--ink)}
.offer svg{width:26px;height:26px;flex:none}
.offer-1{top:40px;font-size:13.5px;line-height:1.15;width:340px}
.offer-2{top:96px;align-items:center}
.offer-2 .price{font-size:30px;font-weight:700}
.offer-2 .price sup{font-size:16px}
.offer-2 span{font-size:13.5px;line-height:1.1}
.offer-3{top:136px;align-items:center;width:345px}
.offer-3 .pct{font-size:26px;font-weight:700;line-height:.85;text-align:center}
.offer-3 .pct small{display:block;font-size:12px}
.offer-3 span{font-size:13.5px;line-height:1.15}
.partners{position:absolute;left:20px;top:498px;width:250px;list-style:none;font-family:"Arimo",Arial,sans-serif}
.partners li{display:flex;gap:10px;align-items:center;margin-bottom:8px;font-size:10px;line-height:1.25;color:var(--text)}
.badge{flex:none;width:44px;height:30px}
.badge-kevo{background:#2f7fc1}
.badge-civic{background:#b7b7b7;height:34px}
.badge-claims{background:#6b8f3a;height:12px;border-radius:6px}
.partners .funds{font-size:12.5px;color:var(--ink);font-family:"Roboto Condensed",sans-serif}
.call{position:absolute;left:302px;top:500px;color:var(--ink)}
.call strong{font-size:15px;font-weight:700;display:block}
.call span{font-size:11px}
.map{left:302px;top:538px;width:215px;height:115px;background:linear-gradient(135deg,#eceae4,#d7dccf)}
.back-footer{position:absolute;left:0;bottom:0;width:530px;height:120px}
.tagline{position:absolute;right:18px;bottom:14px;color:var(--yellow);font-style:italic;font-weight:700;font-size:17px}
</style>
</head>
<body>

<section class="flyer flyer-front">
  <svg class="front-header" viewBox="0 0 530 125" aria-hidden="true">
    <path d="M0 0H530V92C440 72 330 74 250 96C170 116 80 108 0 80Z" fill="var(--blue)"/>
    <path d="M0 90C80 118 170 126 250 106C330 84 440 82 530 102" fill="none" stroke="var(--lime)" stroke-width="4"/>
  </svg>
  <div class="brand" style="right:20px;top:26px">
    <span class="brand-dot"></span>
    <span class="brand-name">Clearway Dental<br>Marrowby</span>
  </div>

  <h1 class="headline">
    <span class="sm">There is</span>
    <span class="lg">NOTHING</span>
    <span class="lg">Better</span>
    <span class="sm">than a</span>
    <span class="lg">Healthy</span>
    <span class="lg">Smile!</span>
  </h1>
  <div class="photo hero-photo" role="img" aria-label="Photo of a smiling family of four"></div>
  <div class="photo lips" role="img" aria-label="Red lips illustration"></div>

  <div class="intro">
    <p>Your sensational smile can become a reality. How do we know? Because we create gorgeous smiles with optimal function every day.</p>
    <p>We specialize in providing top-quality cosmetic and esthetic restorative treatments, so you can rest assured that you're in good hands.</p>
    <p>Our team of qualified dentists will provide regular preventive dental care, including checkups and cleanings, to lay the groundwork for lasting oral</p>
  </div>

  <h2 class="contact-title"><b>Contact</b> Us Today!</h2>
  <ul class="contact-list">
    <li class="phone">
      <svg viewBox="0 0 16 16"><path d="M2 5c0-2 2-3 6-3s6 1 6 3v1h-3V5H5v1H2zM4 7h8l2 6H2z" fill="#222"/></svg>
      <span><strong>(02) 5550 4182</strong> to book an appointment now!</span>
    </li>
    <li>
      <svg viewBox="0 0 16 16"><circle cx="8" cy="8" r="7" fill="#222"/><path d="M8 4v4h3" stroke="#fff" stroke-width="1.6" fill="none"/></svg>
      <div class="hours">
        <span>Office Hours:</span><span>Monday 8:30am – 5:30pm</span>
        <span></span><span>Tuesday 12:00pm – 8:00pm</span>
        <span></span><span>Wednesday – Friday 8:30am – 5:30pm</span>
        <span></span><span>Saturday 9:00am – 4:00pm</span>
      </div>
    </li>
    <li>
      <svg viewBox="0 0 16 16"><path d="M8 1a5 5 0 0 1 5 5c0 4-5 9-5 9S3 10 3 6a5 5 0 0 1 5-5z" fill="#222"/><circle cx="8" cy="6" r="2" fill="#fff"/></svg>
      <span>18 Wattlebrook Avenue Marrowby NSW 2999</span>
    </li>
    <li>
      <svg viewBox="0 0 16 16" fill="none" stroke="#222" stroke-width="1.3"><circle cx="8" cy="8" r="6.5"/><ellipse cx="8" cy="8" rx="3" ry="6.5"/><path d="M1.5 8h13M2.5 5h11M2.5 11h11"/></svg>
      <span>www.clearwaydentalmarrowby.example.au</span>
    </li>
  </ul>
  <div class="photo smile-photo" role="img" aria-label="Close-up photo of a bright smile"></div>

  <div class="front-band"><p>We provide quality dental care at affordable prices.</p></div>
</section>

<section class="flyer flyer-back">
  <div class="photo p1" role="img" aria-label="Photo of a dentist at work"></div>
  <div class="photo p2" role="img" aria-label="Photo of a patient in the dental chair"></div>
  <div class="photo p3" role="img" aria-label="Photo of a dental assistant in safety glasses"></div>
  <div class="photo p4" role="img" aria-label="Photo of a senior dentist"></div>
  <div class="photo doctor" role="img" aria-label="Photo of a dentist in a white coat"></div>

  <div class="services">
    <h2>~ OUR SERVICES ~</h2>
    <ul>
      <li><svg viewBox="0 0 16 16"><rect width="16" height="16" fill="var(--lime)"/><path d="M3 8l3 3 7-7" stroke="#1f1f1f" stroke-width="2.4" fill="none"/></svg>Checkup &amp; Clean</li>
      <li><svg viewBox="0 0 16 16"><rect width="16" height="16" fill="var(--lime)"/><path d="M3 8l3 3 7-7" stroke="#1f1f1f" stroke-width="2.4" fill="none"/></svg>Child Friendly Dentistry</li>
      <li><svg viewBox="0 0 16 16"><rect width="16" height="16" fill="var(--lime)"/><path d="M3 8l3 3 7-7" stroke="#1f1f1f" stroke-width="2.4" fill="none"/></svg>Crowns</li>
      <li><svg viewBox="0 0 16 16"><rect width="16" height="16" fill="var(--lime)"/><path d="M3 8l3 3 7-7" stroke="#1f1f1f" stroke-width="2.4" fill="none"/></svg>Dentures</li>
      <li><svg viewBox="0 0 16 16"><rect width="16" height="16" fill="var(--lime)"/><path d="M3 8l3 3 7-7" stroke="#1f1f1f" stroke-width="2.4" fill="none"/></svg>Extraction</li>
      <li><svg viewBox="0 0 16 16"><rect width="16" height="16" fill="var(--lime)"/><path d="M3 8l3 3 7-7" stroke="#1f1f1f" stroke-width="2.4" fill="none"/></svg>Root Canal Treatment</li>
      <li><svg viewBox="0 0 16 16"><rect width="16" height="16" fill="var(--lime)"/><path d="M3 8l3 3 7-7" stroke="#1f1f1f" stroke-width="2.4" fill="none"/></svg>Same Day Emergency</li>
      <li><svg viewBox="0 0 16 16"><rect width="16" height="16" fill="var(--lime)"/><path d="M3 8l3 3 7-7" stroke="#1f1f1f" stroke-width="2.4" fill="none"/></svg>Tooth Replacement (Bridges)</li>
      <li><svg viewBox="0 0 16 16"><rect width="16" height="16" fill="var(--lime)"/><path d="M3 8l3 3 7-7" stroke="#1f1f1f" stroke-width="2.4" fill="none"/></svg>White Fillings</li>
      <li><svg viewBox="0 0 16 16"><rect width="16" height="16" fill="var(--lime)"/><path d="M3 8l3 3 7-7" stroke="#1f1f1f" stroke-width="2.4" fill="none"/></svg>Whitening</li>
    </ul>
  </div>

  <div class="offers">
    <h2>~ SPECIAL OFFERS ~</h2>
    <div class="offer offer-1">
      <svg viewBox="0 0 24 24"><path d="M12 1l3.2 7 7.6.8-5.7 5.1 1.6 7.5L12 17.6 5.3 21.4l1.6-7.5L1.2 8.8 8.8 8z" fill="var(--teal)"/></svg>
      <p>NO GAP Checkup and Clean with any major Private Health Fund. Includes oral exam, 2 X-Rays, Scale &amp; Polish and Fluoride Treatment.</p>
    </div>
    <div class="offer offer-2">
      <svg viewBox="0 0 24 24"><path d="M12 1l3.2 7 7.6.8-5.7 5.1 1.6 7.5L12 17.6 5.3 21.4l1.6-7.5L1.2 8.8 8.8 8z" fill="var(--teal)"/></svg>
      <span class="price"><sup>$</sup>199</span>
      <span>Genuine Teeth Whitening<br>(usually $399 save $200)</span>
    </div>
    <div class="offer offer-3">
      <svg viewBox="0 0 24 24"><path d="M12 1l3.2 7 7.6.8-5.7 5.1 1.6 7.5L12 17.6 5.3 21.4l1.6-7.5L1.2 8.8 8.8 8z" fill="var(--teal)"/></svg>
      <span class="pct">10%<small>OFF</small></span>
      <span>on all major dental. Includes fillings, crowns, bridges and root canal treatment.</span>
    </div>
  </div>

  <ul class="partners">
    <li><span class="badge badge-kevo"></span><span>We are KEVO Preferred Provider means KEVO members get maximum benefit.</span></li>
    <li><span class="badge badge-civic"></span><span>We participate in Office of Civic Pensions Fee Schedule.</span></li>
    <li><span class="badge badge-claims"></span><span class="funds">WE ACCEPT ALL HEALTH FUNDS</span></li>
  </ul>

  <div class="call">
    <strong>CALL TODAY &nbsp;(02) 5550 4182</strong>
    <span>18 Wattlebrook Avenue Marrowby NSW 2999</span>
  </div>
  <div class="photo map" role="img" aria-label="Orbix Map street map showing the practice location"></div>

  <svg class="back-footer" viewBox="0 0 530 120" aria-hidden="true">
    <path d="M0 30C90 10 170 10 250 28C340 48 440 40 530 20V120H0Z" fill="var(--blue)"/>
    <path d="M0 22C90 2 170 2 250 20C340 40 440 32 530 12" fill="none" stroke="var(--lime)" stroke-width="4"/>
  </svg>
  <div class="brand" style="left:28px;bottom:44px">
    <span class="brand-dot"></span>
    <span class="brand-name">Clearway Dental<br>Marrowby</span>
  </div>
  <p class="tagline">Proudly serving “Lower North Shore” since 1958.</p>
</section>

</body>
</html>
```